Orthodontist Needs Promotional Discount Postcard

5.5 x 8.5 Horizontal 2-Sided Postcard for mailing.
Images & Logo on both sides okay; must be free stock Images from legit sources only, or use attached images. See our website for information, ShoreLaneSmiles.com
Context to include:
New Patient Special $500 off Braces or Clear Aligners
Cannot be combined with any other discounts.
Major dental insurance plans and Cara-Plan accepted
Affordable payment options are available
Call to schedule your free consultation
Present this new patient offer to receive your discount.
Offer ends January 31, 2022.
805-472-9186 www. ShoreLaneSmiles.com
462 N. Harlow Street, Suite B, Ventura, CA 93001-2718
office@shorelanesmiles.com

```html
<!DOCTYPE html>
<html lang="en">
<head>
<meta charset="utf-8">
<title>ShoreLane Smiles – New Patient Postcard</title>
<link rel="stylesheet" href="https://fonts.googleapis.com/css2?family=Arimo:wght@400;700&family=Oswald:wght@300&family=Source+Sans+3:wght@400&display=swap">
<style>
  :root{
    --blue:#2ea7df;
    --gray:#6d6e71;
    --dark:#2a2220;
    --ink:#231f20;
    --white:#ffffff;
    --skin-a:#3b2c26;
    --skin-b:#a0705a;
    --skin-c:#d9a48a;
  }
  *{margin:0;padding:0;box-sizing:border-box}
  html,body{width:979px;height:1200px;overflow:hidden;background:var(--white)}
  body{position:relative;font-family:"Arimo",Arial,sans-serif;color:var(--ink)}
  .card{position:absolute;left:113px;width:1337px;height:865px;transform:scale(0.567);transform-origin:0 0;overflow:hidden;background:var(--white);box-shadow:0 0 6px rgba(0,0,0,.25)}
  .card--front{top:105px}
  .card--back{top:611px}
  .card svg.shapes{position:absolute;inset:0;width:1337px;height:865px}
  .abs{position:absolute}
  .brand{display:flex;align-items:center;gap:28px}
  .brand__dot{width:150px;height:150px;border-radius:50%;background:var(--blue);flex:none}
  .brand__name{color:var(--blue);font-weight:400;font-size:64px;line-height:1.05;letter-spacing:2px}
  .front .brand{left:75px;top:75px}
  .offer__kicker{left:73px;top:428px;color:var(--white);font-size:35px}
  .offer__amount{left:70px;top:478px;color:var(--white);font-size:104px;font-weight:700;letter-spacing:-1px}
  .offer__product{left:73px;top:590px;color:var(--white);font-size:35px}
  .offer__deadline{left:157px;top:642px;width:304px;height:40px;background:var(--white);border-radius:4px;color:var(--gray);font-family:"Oswald",sans-serif;font-weight:300;font-size:30px;line-height:40px;text-align:center}
  .present{left:470px;top:435px;width:210px;height:210px;color:var(--white);font-family:"Oswald",sans-serif;font-weight:300;font-size:29px;line-height:31px;text-align:center;display:flex;align-items:center;justify-content:center}
  .web-links{left:75px;top:738px;color:var(--white);font-size:27px;line-height:28px}
  .web-links li{list-style:none;display:flex;align-items:center;gap:12px}
  .web-links svg{width:24px;height:24px}
  .call__icon{left:676px;top:705px;width:104px;height:88px}
  .call__label{left:800px;top:700px;color:var(--white);font-size:27px}
  .call__number{left:798px;top:730px;color:var(--blue);font-size:68px;font-weight:700;letter-spacing:-1px}
  .terms{left:90px;top:62px;color:var(--white);font-family:"Source Sans 3",sans-serif;font-size:28px;line-height:39.5px}
  .terms li{list-style:none;position:relative;padding-left:30px}
  .terms li::before{content:"";position:absolute;left:0;top:16px;width:11px;height:11px;border-radius:50%;background:var(--white)}
  .stamp{left:1127px;top:75px;width:136px;height:135px;border:1.5px solid var(--ink)}
  .blurb{left:75px;top:445px;width:660px;font-size:22.5px;line-height:22px}
  .back .brand{left:75px;top:600px;flex-direction:column;gap:18px;align-items:center;width:290px}
  .back .brand__dot{width:106px;height:106px}
  .back .brand__name{font-size:46px;text-align:center}
  .contact{left:411px;top:615px}
  .contact__title{color:var(--blue);font-size:36px;font-weight:700;margin-bottom:18px}
  .contact address{font-style:normal;font-size:20px;line-height:21px;margin-bottom:20px}
  .contact ul{font-size:20px;line-height:21px}
  .contact li{list-style:none;display:flex;align-items:center;gap:6px}
  .contact li svg{width:13px;height:13px}
</style>
</head>
<body>

<section class="card card--front front">
  <svg class="shapes" viewBox="0 0 1337 865" aria-hidden="false">
    <defs>
      <linearGradient id="photoTone" x1="0" y1="0" x2="1" y2="0.4">
        <stop offset="0" stop-color="#c9b79c"/>
        <stop offset="0.3" stop-color="var(--skin-a)"/>
        <stop offset="0.65" stop-color="var(--skin-b)"/>
        <stop offset="1" stop-color="var(--skin-c)"/>
      </linearGradient>
      <radialGradient id="mouthTone" cx="0.5" cy="0.5" r="0.5">
        <stop offset="0" stop-color="#f1d2c8"/>
        <stop offset="1" stop-color="#c98b80"/>
      </radialGradient>
    </defs>
    <rect role="img" aria-label="Close-up photo of a woman's bright smile" x="0" y="0" width="1337" height="700" fill="url(#photoTone)"/>
    <path d="M0 0 H1337 V60 C1100 40 900 180 700 260 C520 330 300 340 120 290 C70 275 30 255 0 235 Z" fill="var(--white)"/>
    <path d="M700 255 C900 160 1100 60 1337 80 V130 C1120 95 920 170 700 255 Z" fill="var(--blue)"/>
    <path d="M0 665 V862 H1337 V585 C1200 600 1000 630 800 670 C600 710 350 720 0 665 Z" fill="var(--gray)"/>
    <path d="M0 365 C120 350 260 360 380 400 C480 435 560 520 620 660 C450 700 250 705 0 670 Z" fill="var(--blue)"/>
    <circle cx="575" cy="540" r="105" fill="var(--dark)"/>
    <circle cx="910" cy="565" r="106" fill="var(--gray)"/>
    <circle role="img" aria-label="Photo of teeth with metal braces" cx="910" cy="565" r="100" fill="url(#mouthTone)"/>
    <circle cx="1157" cy="565" r="106" fill="var(--gray)"/>
    <circle role="img" aria-label="Photo of a clear aligner being fitted" cx="1157" cy="565" r="100" fill="url(#mouthTone)"/>
  </svg>

  <div class="brand abs">
    <span class="brand__dot"></span>
    <span class="brand__name">SHORELANE<br>SMILES</span>
  </div>

  <p class="offer__kicker abs">New Patient Special</p>
  <p class="offer__amount abs">$500 off</p>
  <p class="offer__product abs">Braces or Clear Aligners</p>
  <p class="offer__deadline abs">Offer ends January 31, 2022</p>

  <p class="present abs">Present this<br>new patient offer<br>to receive<br>your discount</p>

  <ul class="web-links abs">
    <li><svg viewBox="0 0 24 24"><rect x="2" y="5" width="20" height="14" fill="none" stroke="#fff" stroke-width="1.6"/><path d="M2 5 L12 13 L22 5" fill="none" stroke="#fff" stroke-width="1.6"/></svg>office@shorelanesmiles.com</li>
    <li><svg viewBox="0 0 24 24"><circle cx="12" cy="12" r="10" fill="none" stroke="#fff" stroke-width="1.4"/><ellipse cx="12" cy="12" rx="4.5" ry="10" fill="none" stroke="#fff" stroke-width="1.2"/><path d="M2 12 H22 M4 7 H20 M4 17 H20" stroke="#fff" stroke-width="1.2"/></svg>www.shorelanesmiles.com</li>
  </ul>

  <svg class="call__icon abs" viewBox="0 0 104 88" aria-label="Phone">
    <path d="M4 30 C4 8 100 8 100 30 L100 36 L78 36 L76 24 C64 18 40 18 28 24 L26 36 L4 36 Z" fill="#fff"/>
    <path d="M22 34 L30 30 H74 L82 34 L94 86 H10 Z" fill="#fff"/>
    <g fill="var(--gray)"><circle cx="42" cy="52" r="3"/><circle cx="52" cy="52" r="3"/><circle cx="62" cy="52" r="3"/><circle cx="42" cy="62" r="3"/><circle cx="52" cy="62" r="3"/><circle cx="62" cy="62" r="3"/><circle cx="42" cy="72" r="3"/><circle cx="52" cy="72" r="3"/><circle cx="62" cy="72" r="3"/></g>
  </svg>
  <p class="call__label abs">Call to Schedule Your Free Consultation</p>
  <p class="call__number abs">805-472-9186</p>
</section>

<section class="card card--back back">
  <svg class="shapes" viewBox="0 0 1337 865">
    <defs>
      <radialGradient id="mouthTone2" cx="0.5" cy="0.5" r="0.5">
        <stop offset="0" stop-color="#f1d2c8"/>
        <stop offset="1" stop-color="#c98b80"/>
      </radialGradient>
    </defs>
    <path d="M0 245 C200 280 420 270 600 210 L610 222 C420 290 200 300 0 268 Z" fill="var(--blue)"/>
    <path d="M0 0 H1337 V85 C1200 30 1000 60 800 160 C620 245 300 270 130 205 C50 170 10 120 0 95 Z" fill="var(--blue)"/>
    <circle cx="148" cy="310" r="107" fill="var(--blue)"/>
    <circle role="img" aria-label="Photo of a clear aligner being fitted" cx="148" cy="310" r="101" fill="url(#mouthTone2)"/>
    <circle cx="372" cy="300" r="90" fill="var(--blue)"/>
    <circle role="img" aria-label="Photo of teeth with metal braces" cx="372" cy="300" r="84" fill="url(#mouthTone2)"/>
  </svg>

  <ul class="terms abs">
    <li>Cannot be combined with any other discounts.</li>
    <li>Major dental insurance plans and Cara-Plan accepted.</li>
    <li>Affordable payment options are available.</li>
  </ul>

  <div class="stamp abs" aria-label="Postage area"></div>

  <p class="blurb abs">While we offer a “paid in full” discount, we also will work with you to make an easy payment plan that fits within your budget, and if you have insurance, we’ll use that too! Our expert team will verify any benefits you have! We will be in touch to find out about your dental insurance!</p>

  <div class="brand abs">
    <span class="brand__dot"></span>
    <span class="brand__name">SHORELANE<br>SMILES</span>
  </div>

  <div class="contact abs">
    <h2 class="contact__title">Contact Us</h2>
    <address>462 N. Harlow Street,<br>Suite B, Ventura, CA 93001-2718</address>
    <ul>
      <li><svg viewBox="0 0 14 14"><path d="M3 1 L5 1 L6 4 L4.5 5.5 C5.5 7.5 6.5 8.5 8.5 9.5 L10 8 L13 9 L13 11 C13 12 12 13 11 13 C6 13 1 8 1 3 C1 2 2 1 3 1 Z" fill="var(--ink)"/></svg>805-472-9186</li>
      <li><svg viewBox="0 0 14 14"><rect x="1" y="3" width="12" height="9" fill="none" stroke="var(--ink)" stroke-width="1.2"/><path d="M1 3 L7 8 L13 3" fill="none" stroke="var(--ink)" stroke-width="1.2"/></svg>office@shorelanesmiles.com</li>
      <li><svg viewBox="0 0 14 14"><circle cx="7" cy="7" r="6" fill="none" stroke="var(--ink)" stroke-width="1"/><ellipse cx="7" cy="7" rx="2.6" ry="6" fill="none" stroke="var(--ink)" stroke-width="0.9"/><path d="M1 7 H13" stroke="var(--ink)" stroke-width="0.9"/></svg>www.ShoreLaneSmiles.com</li>
    </ul>
  </div>
</section>

</body>
</html>
```